New Company Business Card Design

I have a new company logo and I want a new business card design. I dont know if the logo file i attached is in the correct format or quality. We are a New York City Specialty construction Firm specializing in high risk out of the box projects. I want a simple and classy business card that people will his card is as crisp as the work his company does.

Target Market(s)

Clients in the heavy construction industry in New York City

Industry/Entity Type

Construction Company

Contact Information for Business Card

Simple Classy - DIFFERENT

Font styles to use
Other font styles liked:
• Mach the logo font in some way

Colors

Designer to choose colors to be used in the design.

Requirements
Must have
• Uniqueness
Nice to have
• Nothing particular - Just different and classy - Timeless
Should not have
• Goofy Shit or Gimmicky shit

```html
<!DOCTYPE html>
<html lang="en">
<head>
<meta charset="utf-8">
<title>Halvrick Associates – Round Business Card</title>
<link rel="stylesheet" href="https://fonts.googleapis.com/css2?family=Arimo:wght@700&family=Open+Sans:wght@400;700&display=swap">
<style>
  :root {
    --backdrop: #5e5e5e;
    --card-blue-light: #1f8fdc;
    --card-blue-mid: #0b74c4;
    --card-blue-deep: #005a9e;
    --card-white: #ffffff;
    --text-white: #ffffff;
    --rule-blue: #5fb6ef;
    --brand-blue: #0a6cb8;
  }
  html, body {
    margin: 0;
    padding: 0;
    width: 1200px;
    height: 900px;
    overflow: hidden;
    background: var(--backdrop);
  }
  .canvas {
    position: relative;
    width: 1200px;
    height: 900px;
    background: var(--backdrop);
  }
  .card {
    position: absolute;
    top: 235px;
    width: 414px;
    height: 414px;
    border-radius: 50%;
    display: flex;
    flex-direction: column;
    align-items: center;
    justify-content: center;
    text-align: center;
  }
  .card--front {
    left: 184px;
    background: radial-gradient(circle at 50% 45%, var(--card-blue-light) 0%, var(--card-blue-mid) 55%, var(--card-blue-deep) 100%);
    color: var(--text-white);
    font-family: "Open Sans", Arial, sans-serif;
  }
  .card--back {
    left: 623px;
    background: var(--card-white);
  }
  .person-name {
    font-family: "Arimo", Arial, sans-serif;
    font-weight: 700;
    font-size: 29px;
    line-height: 32px;
    letter-spacing: 0.3px;
    margin: 0;
  }
  .person-role {
    font-size: 19px;
    line-height: 24px;
    margin: 0;
  }
  .rule {
    width: 196px;
    height: 1px;
    background: var(--rule-blue);
    margin: 13px 0 12px;
  }
  .rule--lower {
    margin: 13px 0 6px;
  }
  .contact-list {
    list-style: none;
    margin: 0;
    padding: 0;
    font-size: 19px;
    line-height: 24.5px;
  }
  .contact-list b {
    font-weight: 700;
  }
  .address {
    margin: 0;
    font-size: 19px;
    line-height: 24.5px;
  }
  .brand-name {
    font-family: "Arimo", Arial, sans-serif;
    font-weight: 700;
    font-size: 25px;
    letter-spacing: 1px;
    color: var(--brand-blue);
    margin: 0;
  }
</style>
</head>
<body>
  <main class="canvas">
    <section class="card card--front" aria-label="Card front">
      <h1 class="person-name">DANIEL CARTER</h1>
      <p class="person-role">Managing Director</p>
      <div class="rule"></div>
      <ul class="contact-list">
        <li><b>P:</b> 044-123 456 789</li>
        <li><b>F:</b> 044-123 456 789</li>
        <li><b>E:</b> info@webname.com</li>
        <li><b>W:</b> www.websitename.com</li>
      </ul>
      <div class="rule rule--lower"></div>
      <p class="address">12345, Address Goes Here<br>Country Name, 123456.</p>
    </section>

    <section class="card card--back" aria-label="Card back">
      <p class="brand-name">HALVRICK ASSOCIATES, INC.</p>
    </section>
  </main>
</body>
</html>
```